Pull Up Banner Design 85cm X200cm

The pull up banner is intended for branding and services awareness purposes, and to be used at exhibition and conference. Please refer to the websites below for more information
1. https://www.brivanta.online/
2. https://www.brivanta.online/landing-page
3. https://blog.brivanta.online/faq-for-client/
4. https://blog.brivanta.online/faq-for-advisor/

Ideally, the banner will lead potential users both young entrepreneurs and online business owners (as clients) to Brivanta marketplace, and also professional services providers like accountants and finance advisors and consultants (as advisors) to sign up with the platform. (Like PixelHarbor marketplace)

Target Market(s)

Business users and accountants aged between 25 to 44 yrs old

Requirements
Must have
• website address (www.brivanta.online)
• and
• company logo "Brivanta" as attached

```html
<!DOCTYPE html>
<html lang="en">
<head>
<meta charset="utf-8">
<title>Brivanta Pull Up Banner</title>
<link href="https://fonts.googleapis.com/css2?family=Montserrat:wght@700&family=Bebas+Neue&family=Signika:wght@500&family=Roboto:wght@500&display=swap" rel="stylesheet">
<style>
  :root {
    --stage: #e6e8eb;
    --banner-blue: #0b77bf;
    --banner-blue-light: #3a9ad8;
    --sky: #b5e1e0;
    --sky-deep: #8fd0cf;
    --navy: #2e4660;
    --cream: #f5e7a6;
    --white: #ffffff;
    --footer: #2b2d31;
    --url-blue: #1a86cf;
    --icon-bg: #7fd0cc;
    --accent-orange: #f7a823;
  }
  * { margin: 0; padding: 0; box-sizing: border-box; }
  html, body { width: 1200px; height: 1200px; overflow: hidden; background: var(--stage); }
  .banner {
    position: absolute; left: 345px; top: 0; width: 510px; height: 1200px;
    background: linear-gradient(180deg, var(--banner-blue-light) 0%, var(--banner-blue) 40%, var(--banner-blue) 100%);
    overflow: hidden;
  }
  .corner { position: absolute; top: 200px; width: 0; height: 0; }
  .corner--left { left: 0; border-top: 110px solid transparent; border-bottom: 110px solid transparent; border-left: 70px solid var(--sky); }
  .corner--right { right: 0; border-top: 110px solid transparent; border-bottom: 110px solid transparent; border-right: 70px solid var(--sky); }
  .hero {
    position: absolute; left: -30px; top: -340px; width: 570px; height: 580px; border-radius: 50%;
    background: radial-gradient(circle at 60% 70%, var(--sky) 0%, var(--sky-deep) 100%);
  }
  .logo { position: absolute; left: 22px; top: 12px; display: flex; flex-direction: column; align-items: center; }
  .logo__mark { width: 44px; height: 44px; border-radius: 50%; background: var(--banner-blue); }
  .logo__name { font-family: 'Montserrat', sans-serif; font-weight: 700; font-size: 24px; color: var(--banner-blue); margin-top: 6px; }
  .title { position: absolute; left: 0; width: 100%; top: 232px; text-align: center; font-family: 'Montserrat', sans-serif; font-weight: 700; font-size: 56px; color: var(--white); }
  .tagline { position: absolute; left: 0; width: 100%; top: 300px; text-align: center; font-family: 'Bebas Neue', sans-serif; font-size: 29px; color: var(--navy); }
  .section-head {
    position: absolute; left: 90px; width: 332px; text-align: center; font-family: 'Bebas Neue', sans-serif;
    font-size: 38px; color: var(--white); border-bottom: 1px solid rgba(255,255,255,.55); padding-bottom: 4px;
  }
  .feature { position: absolute; left: 0; width: 510px; }
  .feature__icon { position: absolute; left: 22px; width: 64px; height: 64px; }
  .feature__title { position: absolute; left: 84px; font-family: 'Roboto', sans-serif; font-weight: 500; font-size: 17.5px; color: var(--white); }
  .feature__text { position: absolute; left: 99px; top: 22px; width: 395px; font-family: 'Signika', sans-serif; font-weight: 500; font-size: 16px; line-height: 21px; color: var(--cream); }
  .footer { position: absolute; left: 0; top: 1082px; width: 510px; height: 118px; background: var(--footer); }
  .footer__corner { position: absolute; bottom: 0; width: 0; height: 0; }
  .footer__corner--left { left: 0; border-top: 110px solid transparent; border-left: 100px solid var(--banner-blue); }
  .footer__corner--right { right: 0; border-top: 110px solid transparent; border-right: 100px solid var(--banner-blue); }
  .footer__globe { position: absolute; left: 234px; top: 16px; }
  .footer__url { position: absolute; left: 0; width: 100%; top: 62px; text-align: center; font-family: 'Bebas Neue', sans-serif; font-size: 36px; color: var(--url-blue); }
</style>
</head>
<body>
<main class="banner">
  <div class="corner corner--left"></div>
  <div class="corner corner--right"></div>
  <div class="hero" role="img" aria-label="Illustration of a smiling consultant working at a laptop, connected to a network of advisor portraits over a city skyline"></div>

  <div class="logo">
    <span class="logo__mark"></span>
    <span class="logo__name">Brivanta</span>
  </div>

  <h1 class="title">Brivanta</h1>
  <p class="tagline">Matches you with the right advisors online!</p>

  <h2 class="section-head" style="top:340px;">Looking for an advisor?</h2>

  <section class="feature" style="top:400px;">
    <svg class="feature__icon" style="top:22px;" viewBox="0 0 64 64" aria-hidden="true">
      <circle cx="32" cy="32" r="31" fill="var(--icon-bg)"/>
      <rect x="10" y="16" width="44" height="30" rx="3" fill="#fff" stroke="#34495e" stroke-width="3"/>
      <rect x="12" y="14" width="40" height="6" fill="#e74c3c"/>
      <circle cx="30" cy="33" r="5" fill="#e74c3c"/>
      <rect x="28" y="46" width="8" height="6" fill="#34495e"/>
    </svg>
    <h3 class="feature__title">ONE-STOP BORDERLESS MARKETPLACE</h3>
    <p class="feature__text">Access instantly to a network of great independent advisors, consultants, industry professionals, boutique firms and small sized practices, including best talents in accounting, finance and strategy all in one place.</p>
  </section>

  <section class="feature" style="top:541px;">
    <svg class="feature__icon" style="top:12px;" viewBox="0 0 64 64" aria-hidden="true">
      <circle cx="36" cy="32" r="30" fill="var(--icon-bg)"/>
      <circle cx="44" cy="16" r="5" fill="#2a5c8a"/>
      <path d="M40 22 L30 36 L40 42 L36 54 M32 34 L22 42 M40 26 L50 32" stroke="#2a5c8a" stroke-width="5" fill="none" stroke-linecap="round"/>
      <path d="M2 28 H18 M6 36 H20 M0 44 H16" stroke="var(--accent-orange)" stroke-width="3" stroke-linecap="round"/>
    </svg>
    <h3 class="feature__title">CONVENIENT AND QUICK</h3>
    <p class="feature__text">Get matched instantly to 3 of the great advisors for you to compare. Then communicate, chat, interview, appoint and sign the engagement online.</p>
  </section>

  <section class="feature" style="top:644px;">
    <svg class="feature__icon" style="top:8px;" viewBox="0 0 64 64" aria-hidden="true">
      <circle cx="32" cy="32" r="31" fill="var(--icon-bg)"/>
      <rect x="12" y="28" width="10" height="24" fill="#2a5c8a"/>
      <path d="M24 28 L34 12 Q40 12 38 24 H50 Q54 26 52 32 L48 52 H24 Z" fill="var(--accent-orange)"/>
    </svg>
    <h3 class="feature__title">HIRE WITH CONFIDENCE</h3>
    <p class="feature__text">Explore each advisors profile and browse their previous works as well as clients review in a simple manner online.</p>
  </section>

  <h2 class="section-head" style="top:742px;">Looking for a project?</h2>

  <section class="feature" style="top:808px;">
    <svg class="feature__icon" style="top:18px;" viewBox="0 0 64 64" aria-hidden="true">
      <rect x="12" y="14" width="56" height="40" rx="4" fill="var(--accent-orange)"/>
      <rect x="12" y="14" width="56" height="6" fill="#f5d23c"/>
      <circle cx="28" cy="32" r="6" fill="#2a5c8a"/>
      <path d="M18 48 Q28 36 38 48 Z" fill="#2a5c8a"/>
      <path d="M44 30 H62 M44 38 H62 M44 46 H58" stroke="#fff" stroke-width="4"/>
    </svg>
    <h3 class="feature__title">PROFESSIONAL PROFILE</h3>
    <p class="feature__text">Let thousands of online users view your profile every month</p>
  </section>

  <section class="feature" style="top:888px;">
    <svg class="feature__icon" style="top:24px;" viewBox="0 0 64 64" aria-hidden="true">
      <rect x="0" y="0" width="46" height="26" rx="2" fill="#5c6fb8"/>
      <path d="M6 6 H16 V10 Q11 18 6 10 Z M11 14 V20 M7 21 H15" stroke="#fff" stroke-width="2" fill="none"/>
      <path d="M20 10 H40 M20 16 H40 M20 22 H36" stroke="#fff" stroke-width="2"/>
      <rect x="26" y="28" width="20" height="24" rx="2" fill="var(--accent-orange)"/>
      <rect x="50" y="6" width="18" height="24" rx="2" fill="var(--icon-bg)"/>
      <circle cx="59" cy="16" r="5" fill="none" stroke="#fff" stroke-width="2"/>
    </svg>
    <h3 class="feature__title">EXPERTISE SHOWCASE</h3>
    <p class="feature__text">Let your success cases and job credentials to be visible online. Users want to connect with you if you have relevant expertise and walked the path before.</p>
  </section>

  <section class="feature" style="top:1005px;">
    <svg class="feature__icon" style="top:20px;" viewBox="0 0 64 64" aria-hidden="true">
      <rect x="0" y="16" width="62" height="20" rx="10" fill="#5c6fb8"/>
      <path d="M34 38 L28 50 H34 L30 60 L42 46 H36 L40 38 Z" fill="#f5d23c"/>
      <path d="M52 4 L62 0 L58 10 L50 16 Z" fill="none" stroke="var(--accent-orange)" stroke-width="2"/>
    </svg>
    <h3 class="feature__title">JOB LEADS</h3>
    <p class="feature__text">You can access to the job leads instantly at the click of a button</p>
  </section>

  <footer class="footer">
    <div class="footer__corner footer__corner--left"></div>
    <div class="footer__corner footer__corner--right"></div>
    <svg class="footer__globe" width="42" height="42" viewBox="0 0 42 42" aria-hidden="true">
      <g fill="none" stroke="#fff" stroke-width="2.5">
        <circle cx="21" cy="21" r="18"/>
        <ellipse cx="21" cy="21" rx="8" ry="18"/>
        <path d="M3 21 H39 M6 12 H36 M6 30 H36"/>
      </g>
    </svg>
    <p class="footer__url">www.brivanta.online</p>
  </footer>
</main>
</body>
</html>
```